Korvel Reefworks business card

We sell live saltwater fish and live corals
Korvel Reefworks
7 Halden Ct
Larkfield, NJ. 08411
(555) 319-7264
Contact Information for Business Card
Korvel Reefworks
7 Halden Ct
Larkfield, NJ. 08411
(555) 319-7264
Colors
Designer to choose colors to be used in the design.

```html
<!DOCTYPE html>
<html lang="en">
<head>
<meta charset="utf-8">
<title>Korvel Reefworks – Business Card</title>
<link href="https://fonts.googleapis.com/css2?family=Alegreya+Sans+SC:wght@700;800&display=swap" rel="stylesheet">
<style>
  :root {
    --backdrop: #262626;
    --card: #ffffff;
    --brand-red: #c8461f;
    --address-green: #1f9a6a;
    --phone-blue: #1c8fbe;
    --rule: #222222;
    --reef-deep: #0f5f6e;
    --reef-sea: #1a8fa6;
    --reef-anemone: #6f7a3a;
    --reef-shadow: #23341f;
  }
  * { margin: 0; padding: 0; box-sizing: border-box; }
  html, body {
    width: 1200px;
    height: 895px;
    overflow: hidden;
    background: var(--backdrop);
  }
  .business-card {
    position: absolute;
    left: 170px;
    top: 201px;
    width: 860px;
    height: 492px;
    background: var(--card);
    border-radius: 30px;
    overflow: hidden;
    display: flex;
    box-shadow: 0 10px 30px rgba(0,0,0,0.45);
  }
  .reef-photo {
    width: 350px;
    flex: 0 0 350px;
    height: 100%;
    background:
      radial-gradient(ellipse at 40% 60%, var(--reef-anemone) 0%, rgba(111,122,58,0.6) 35%, transparent 65%),
      radial-gradient(ellipse at 30% 95%, var(--reef-shadow) 0%, transparent 55%),
      linear-gradient(160deg, var(--reef-sea) 0%, var(--reef-deep) 55%, #2e6f55 100%);
  }
  .card-details {
    flex: 1;
    display: flex;
    flex-direction: column;
    align-items: center;
    justify-content: center;
    text-align: center;
    font-family: "Alegreya Sans SC", sans-serif;
    font-variant-numeric: lining-nums;
    padding: 0 24px 10px;
  }
  .brand-name {
    color: var(--brand-red);
    font-weight: 800;
    font-size: 46px;
    letter-spacing: 1px;
    line-height: 1;
    white-space: nowrap;
  }
  .divider {
    width: 74px;
    height: 2px;
    background: var(--rule);
    margin: 30px 0;
  }
  .address {
    color: var(--address-green);
    font-weight: 700;
    font-size: 20px;
    letter-spacing: 3px;
    line-height: 1.35;
    white-space: nowrap;
  }
  .phone {
    color: var(--phone-blue);
    font-weight: 700;
    font-size: 40px;
    letter-spacing: 2px;
    line-height: 1;
    white-space: nowrap;
  }
</style>
</head>
<body>
  <div class="business-card">
    <div class="reef-photo" role="img" aria-label="Underwater photo of clownfish swimming among a green anemone on a coral reef"></div>
    <div class="card-details">
      <div class="brand-name">KORVEL REEFWORKS</div>
      <div class="divider"></div>
      <div class="address">
        <div>7 HALDEN CT, LARKFIELD</div>
        <div>NJ. 08411</div>
      </div>
      <div class="divider"></div>
      <div class="phone">(555) 319-7264</div>
    </div>
  </div>
</body>
</html>
```